Vorla Advise Business Cards

We need a business card design for Vorla Advise (Logo Attached), a management consultancy specialized in brand & business building.

Design should be clean, smart and a touch of innnovation without being gimmicky.

The details on the card should be:
Name: Tomas Vellaquin
Title: Managing Director
Address: 42 Marden Wharf, Kestrel Tower Building, Singapore 073296
Tel: +6284729156048
email: tv@vorlaadvise.example
website: vorlaadvise.example

For further background on corporate identity, please check www.vorlaadvise.example
Updates

Dear all,

Many thanks for the submissions so far! I gave feedback to those designs that I prefer at this stage.

Overall I see that my preference goes into the direction that 'less is more' and 'simple is beautiful'

Please create uniqueness and standout by the simplicity and attraction of the overall concept and design.

Many thanks and please shout incase of questions!

Tomas

Industry/Entity Type

Business

```html
<!DOCTYPE html>
<html lang="en">
<head>
<meta charset="utf-8">
<title>Vorla Advise Business Cards</title>
<link rel="stylesheet" href="https://fonts.googleapis.com/css2?family=Carlito:wght@400;700&display=swap">
<style>
  :root {
    --board: #413836;
    --card: #ffffff;
    --ink: #3f3f3f;
    --accent: #e8601c;
    --rule: #4a4a4a;
  }
  * { box-sizing: border-box; margin: 0; padding: 0; }
  html, body { width: 1200px; height: 849px; overflow: hidden; }
  body {
    background: var(--board);
    font-family: "Carlito", "Calibri", sans-serif;
    color: var(--ink);
    position: relative;
  }
  .card {
    position: absolute;
    width: 458px;
    height: 275px;
    background: var(--card);
    box-shadow: 0 1px 3px rgba(0,0,0,0.35);
  }
  .card--front-a { left: 93px; top: 98px; }
  .card--back-a  { left: 644px; top: 98px; }
  .card--back-b  { left: 93px; top: 476px; }
  .card--front-b { left: 644px; top: 476px; }

  .wordmark {
    position: absolute;
    font-weight: 400;
    font-size: 32px;
    letter-spacing: 0.3px;
    color: var(--ink);
    line-height: 1;
    white-space: nowrap;
  }
  .card--front-a .wordmark { left: 0; right: 0; text-align: center; top: 104px; }
  .card--back-a .wordmark { left: 27px; top: 227px; }

  .tagline {
    position: absolute;
    left: 0; right: 0;
    text-align: center;
    font-size: 13.5px;
    letter-spacing: 0.3px;
    text-transform: uppercase;
    white-space: nowrap;
  }
  .tagline .amp { color: var(--accent); }
  .card--back-b .tagline { top: 122px; }
  .card--front-b .tagline { top: 109px; }

  .contact {
    position: absolute;
    border-left: 1px solid var(--rule);
    padding-left: 10px;
    font-size: 12px;
    line-height: 15px;
    white-space: nowrap;
  }
  .contact__name, .contact__label { color: var(--accent); }
  .card--front-a .contact--person { left: 29px; top: 197px; }
  .card--front-a .contact--reach  { left: 273px; top: 212px; }
  .card--front-b .contact--person { left: 32px; top: 195px; }
  .card--front-b .contact--reach  { left: 274px; top: 210px; }
</style>
</head>
<body>
  <section class="card card--front-a">
    <div class="wordmark">Vorla Advise</div>
    <div class="contact contact--person">
      <div class="contact__name">Tomas Vellaquin</div>
      <div>Managing Director</div>
      <div>42 Marden Wharf, Kestrel Tower Building,</div>
      <div>Singapore 073296</div>
    </div>
    <div class="contact contact--reach">
      <div><span class="contact__label">Tel:</span> +6284729156048</div>
      <div><span class="contact__label">email:</span> tv@vorlaadvise.example</div>
      <div><span class="contact__label">website:</span> vorlaadvise.example</div>
    </div>
  </section>

  <section class="card card--back-a">
    <div class="wordmark">Vorla Advise</div>
  </section>

  <section class="card card--back-b">
    <p class="tagline">Consumer-Centric Brand <span class="amp">&amp;</span> Business Building</p>
  </section>

  <section class="card card--front-b">
    <p class="tagline">Consumer-Centric Brand <span class="amp">&amp;</span> Business Building</p>
    <div class="contact contact--person">
      <div class="contact__name">Tomas Vellaquin</div>
      <div>Managing Director</div>
      <div>42 Marden Wharf, Kestrel Tower Building,</div>
      <div>Singapore 073296</div>
    </div>
    <div class="contact contact--reach">
      <div><span class="contact__label">Tel:</span> +6284729156048</div>
      <div><span class="contact__label">email:</span> tv@vorlaadvise.example</div>
      <div><span class="contact__label">website:</span> vorlaadvise.example</div>
    </div>
  </section>
</body>
</html>
```